New Business Card Design for Houston-based Office Building Association

We need a business card design for our membership association in Houston known at Houston TREVA (Houston Tower Lessors & Operators Guild). Our members are office building managers and vendors in the commercial real estate industry. Any building imagery should be of office buildings, skyscrapers, skylines, etc. (Please do NOT use houses or residential homes.) The final design should be clean and cohesive utilizing our logo and branding. I've attached our logos, branding guide, and the information to be included on the business cards.

Target Market(s)

Professionals in office buildings and commercial real estate. Our market is conservative, modern and upmarket.

Contact Information for Business Card

Should include: name, title, email, direct phone number, cell phone number, address, and possibly website. Our address is 14 Larkmont Court, Suite 200, Houston TX 77052. Our website is houstontreva.example. Other fields should be editable for each employee.

Colors
ffffff
33b8a4
86cfc6
00a990

Requirements
Must have
• Clean, professional, modern, look, integrating our branding, logo and colors. Our logo font is Gotham Light and signature color is PMS color Pantone 2401C (hex code 40a89d.) Our accent color is PMS color Pantone Cool Gray 10C (hex code: 636466)
Should not have
• NO imagery of homes or residential houses. We represent commercial real estate/office buildings only.

```html
<!DOCTYPE html>
<html lang="en">
<head>
<meta charset="utf-8">
<title>Houston TREVA – Business Card</title>
<link rel="stylesheet" href="https://fonts.googleapis.com/css2?family=Montserrat:wght@300;400&display=swap">
<style>
  :root {
    --brand-teal: #40a89d;
    --teal-deep: #37a598;
    --cool-gray: #636466;
    --stripe-gray: #737476;
    --paper: #ffffff;
    --backdrop: #2e2e2f;
  }
  * { box-sizing: border-box; margin: 0; padding: 0; }
  html, body {
    width: 1200px; height: 880px; overflow: hidden;
    background: var(--backdrop);
    font-family: "Montserrat", sans-serif;
  }
  .canvas { position: relative; width: 1200px; height: 880px; }

  .card {
    position: absolute; width: 560px; height: 320px;
    border-radius: 20px; overflow: hidden;
    box-shadow: 0 14px 30px rgba(0,0,0,.45);
  }

  /* Back side */
  .card-back { left: 110px; top: 70px; background: var(--brand-teal); }
  .card-back .pattern-area {
    position: absolute; inset: 0; background: var(--teal-deep);
  }
  .back-lockup {
    position: absolute; right: 34px; top: 118px;
    display: flex; align-items: center; gap: 12px;
  }
  .back-lockup .mark-dot {
    width: 62px; height: 62px; border-radius: 50%; background: var(--paper);
  }
  .back-lockup .brand-name {
    color: var(--paper); font-weight: 400; font-size: 17px;
    white-space: nowrap;
  }

  /* Front side */
  .card-front { left: 530px; top: 480px; background: var(--paper); }
  .card-front .wave { position: absolute; inset: 0; }

  .front-lockup {
    position: absolute; left: 36px; top: 46px;
    display: flex; align-items: center; gap: 16px;
  }
  .front-lockup .mark-dot {
    width: 88px; height: 88px; border-radius: 50%; background: var(--brand-teal);
  }
  .front-lockup .brand-name {
    color: var(--cool-gray); font-weight: 400; font-size: 24px;
    white-space: nowrap;
  }

  .person { position: absolute; left: 36px; top: 162px; }
  .person .name {
    color: var(--cool-gray); font-weight: 400; font-size: 20px;
    letter-spacing: 1.5px; text-transform: uppercase;
  }
  .person .title { color: var(--brand-teal); font-size: 14px; font-weight: 400; margin-top: 2px; }

  .contact-list {
    position: absolute; left: 36px; top: 212px; list-style: none;
  }
  .contact-list li {
    display: flex; align-items: center; gap: 8px;
    color: var(--cool-gray); font-size: 13px; line-height: 1; height: 19px;
    white-space: nowrap;
  }
  .contact-list .icon {
    width: 15px; height: 15px; border-radius: 50%;
    background: var(--brand-teal); flex: none;
  }
</style>
</head>
<body>
<main class="canvas">

  <section class="card card-back" aria-label="Card back">
    <div class="pattern-area" role="img" aria-label="Repeating tonal pattern of the association's building emblem"></div>
    <div class="back-lockup">
      <span class="mark-dot"></span>
      <span class="brand-name">Houston TREVA</span>
    </div>
  </section>

  <section class="card card-front" aria-label="Card front">
    <svg class="wave" width="560" height="320" viewBox="0 0 560 320" aria-hidden="true">
      <path fill="var(--stripe-gray)" d="M414 0 C466 70 438 150 498 240 C518 270 544 290 560 296 L560 0 Z"/>
      <path fill="var(--paper)" d="M432 0 C484 70 456 150 514 232 C534 258 550 272 560 277 L560 0 Z"/>
      <path fill="var(--brand-teal)" d="M446 0 C498 70 470 150 528 224 C542 242 552 250 560 254 L560 0 Z"/>
    </svg>

    <div class="front-lockup">
      <span class="mark-dot"></span>
      <span class="brand-name">Houston TREVA</span>
    </div>

    <div class="person">
      <p class="name">Nolan Reyes</p>
      <p class="title">Owner</p>
    </div>

    <ul class="contact-list">
      <li><svg class="icon" viewBox="0 0 14 14"><rect x="4.5" y="3" width="5" height="8" rx="1" fill="#fff"/></svg>(555) 014-2290</li>
      <li><svg class="icon" viewBox="0 0 14 14"><rect x="3.5" y="6" width="7" height="4" rx="1" fill="#fff"/><rect x="3" y="4" width="8" height="1.5" rx=".7" fill="#fff"/></svg>(555) 014-2290</li>
      <li><svg class="icon" viewBox="0 0 14 14"><rect x="3.5" y="4.5" width="7" height="5" fill="#fff"/><path d="M3.5 4.5 L7 7.5 L10.5 4.5" stroke="#40a89d" stroke-width=".8" fill="none"/></svg>info@treva-mail.example</li>
      <li><svg class="icon" viewBox="0 0 14 14"><circle cx="7" cy="7" r="3.6" fill="none" stroke="#fff" stroke-width="1"/><path d="M3.4 7 H10.6 M7 3.4 V10.6" stroke="#fff" stroke-width=".8"/></svg>houstontreva.example</li>
      <li><svg class="icon" viewBox="0 0 14 14"><path d="M7 11 C5 8.5 4.5 7.5 4.5 6.2 A2.5 2.5 0 0 1 9.5 6.2 C9.5 7.5 9 8.5 7 11 Z" fill="#fff"/></svg>14 Larkmont Court, Suite 200, Houston TX 77052</li>
    </ul>
  </section>

</main>
</body>
</html>
```